We are wanting Flagpole Technical Spec sheets custom to our company of which certain fields are editable per project to submit to architects/engineers in pdf format.
Examples 1 and 2 attached are good basic oneline details, however not very fancy and limited in details on bottom right are specific to one flagpole.
Examples 3 and 4 have better graphics however limited in details on bottom right are specific to one flagpole.
we would like a two page spec sheet. 1st page removes specifications and the second page would have flagpole specifications similar to Examples 5 and 6
page 1 editable fields would be; customer and/or job name, date, part number, notes
page 2 would like to be able to highlight, make bold, have stand out the entire line of the specific flagpole catalog number so as to show it matches the catalog number on page 1
the final design will need to include our logo attached as well as contact information at the footer as seen on examples 1 and 2

```html
<!DOCTYPE html>
<html lang="en">
<head>
<meta charset="utf-8">
<title>Ridgeline Flag &amp; Flagpole – Spec Sheet</title>
<link href="https://fonts.googleapis.com/css2?family=Poppins:wght@400;500;600;700&family=Roboto+Condensed:wght@400;700&family=Arimo:wght@400;700&display=swap" rel="stylesheet">
<style>
:root{
  --bg:#6e6e6e;
  --paper:#ffffff;
  --red:#8a1a1e;
  --gold:#a99a6b;
  --gold-light:#bfb185;
  --ink:#2a2a2a;
  --navy:#2b2b3c;
  --grid:#9a9a9a;
  --row-alt:#ededed;
}
*{box-sizing:border-box;margin:0;padding:0}
html,body{width:862px;height:1200px;overflow:hidden;background:var(--bg)}
body{position:relative;font-family:"Poppins",sans-serif;color:var(--ink)}
.page{position:absolute;top:312px;width:410px;height:575px;background:var(--paper);overflow:hidden}
.page--drawing{left:16px}
.page--specs{left:436px}

/* ---------- page 1 ---------- */
.brand{position:absolute;left:18px;top:34px;width:90px;text-align:center;display:flex;flex-direction:column;align-items:center;gap:4px}
.brand__dot{width:12px;height:12px;border-radius:50%;background:var(--gold)}
.brand__name{font-weight:700;font-size:10px;line-height:1.15;color:var(--navy)}
.field{position:absolute;border:1px solid var(--gold);height:10px;display:flex;align-items:stretch}
.field__label{background:var(--gold);color:#fff;font-size:6px;padding:0 3px;line-height:8px;white-space:nowrap}
.field--customer{left:113px;top:24px;width:273px}
.field--date{left:113px;top:38px;width:112px}
.field--part{left:231px;top:38px;width:155px}
.field--notes{left:113px;top:52px;width:273px;height:47px;align-items:flex-start}

.pole-art{position:absolute;left:22px;top:155px;width:90px;height:316px;
  background:linear-gradient(90deg,#f4f4f2 0%,#dfe2e4 45%,#e8e4d8 100%)}
.callout{position:absolute;left:115px;font-family:"Roboto Condensed",sans-serif;font-size:4.8px;line-height:1.2;color:#333;width:150px}
.callout b{font-size:5.4px;font-weight:700}
.callout::before{content:"";position:absolute;left:-14px;top:3px;width:12px;border-top:0.6px solid #333}
.note{position:absolute;left:188px;top:434px;width:50px;font-family:"Roboto Condensed",sans-serif;font-size:3.6px;line-height:1.25;color:#444}

.partno{position:absolute;top:146px;height:20px;border:1px solid #555;font-family:"Arimo",sans-serif;font-weight:700;font-size:12px;display:flex;align-items:center;justify-content:center}
.partno--model{left:245px;width:85px}
.partno--finish{left:343px;width:43px}
.partno__dash{position:absolute;left:334px;top:149px;font-family:"Arimo",sans-serif;font-weight:700;font-size:11px}

.product{position:absolute;width:62px;font-family:"Arimo",sans-serif;font-size:5.6px;line-height:1.2;color:#222}
.product__img{width:55px;height:61px;border:0.6px solid #777;margin-bottom:3px}
.product__code{font-weight:700;font-size:6px}
.img-truck{background:radial-gradient(circle at 50% 40%,#f3f4f5,#b9bec3 70%,#fff 72%)}
.img-ball{background:radial-gradient(circle at 45% 35%,#f2dc95,#b88f2c 45%,#fff 47%)}
.img-collar{background:radial-gradient(ellipse at 50% 50%,#fff 12%,#c9cdd1 14%,#eef0f2 38%,#fff 52%)}
.img-satin{background:linear-gradient(90deg,#8f969c,#eef0f1 40%,#b4babf 70%,#7d848a)}
.img-cleat{background:linear-gradient(90deg,#b8bdc2,#eceeef 50%,#c9a85a 55%,#aeb3b8)}

.footer{position:absolute;left:0;right:0;top:531px;height:25px;background:var(--red)}
.footer__brand{position:absolute;left:24px;top:533px;color:#fff;font-size:8.5px;font-weight:500;line-height:1.05}
.footer__brand small{display:block;font-size:7px;font-weight:400}
.footer__address{position:absolute;left:133px;top:523px;width:150px;height:33px;background:var(--gold);
  clip-path:polygon(4% 0,100% 0,96% 100%,0 100%);color:#fff;font-size:6.4px;white-space:nowrap;display:flex;align-items:center;justify-content:center}
.footer__contact{position:absolute;left:303px;top:534px;color:#fff;font-size:7px;line-height:1.35}
.footer__contact div{display:flex;align-items:center;gap:4px;white-space:nowrap}
.footer__contact svg{width:6px;height:6px;fill:#fff}

/* ---------- page 2 ---------- */
.specs__title{position:absolute;left:12px;top:21px;font-size:10.2px;font-weight:700;color:#111;white-space:nowrap}
.specs__title span{font-weight:400;color:#555}
.spec-table{position:absolute;left:6px;top:42px;width:398px;border-collapse:collapse;table-layout:fixed;font-size:5.8px}
.spec-table th{background:var(--red);color:#fff;font-weight:400;text-align:left;font-size:6.4px;line-height:1.05;padding:2px 3px;height:21px;vertical-align:middle;white-space:nowrap}
.spec-table th small{display:inline-block;font-size:3.4px;border:0.5px solid #fff;padding:0 1px;margin-top:1px}
.spec-table td{height:13.5px;text-align:center;border:0.5px solid var(--grid);padding:0}
.spec-table tbody tr:nth-child(even) td{background:var(--row-alt)}
.spec-table td.cat{background:var(--gold);color:#2a2a2a}
.spec-table tbody tr:nth-child(even) td.cat{background:var(--gold-light)}
</style>
</head>
<body>

<section class="page page--drawing">
  <div class="brand"><span class="brand__dot"></span><span class="brand__name">Ridgeline<br>Flag &amp; Flagpole</span></div>

  <div class="field field--customer"><span class="field__label">Customer / Job Name</span></div>
  <div class="field field--date"><span class="field__label">Date:</span></div>
  <div class="field field--part"><span class="field__label">Part Number:</span></div>
  <div class="field field--notes"><span class="field__label">Notes:</span></div>

  <div class="pole-art" role="img" aria-label="Dimensioned elevation drawing of the flagpole with set depth and ground sleeve foundation section"></div>

  <div class="callout" style="top:157px"><b>Truck and Ornament</b> (Options Available)<br>See Specification Box</div>
  <div class="callout" style="top:190px">Halyard Assembly, #10 (5/16" Diameter)<br>Polyester Rope</div>
  <div class="callout" style="top:214px">Two (2) Stainless Steel Swivel Flagsnaps and<br>Two (2) Neoprene Flagsnap Covers</div>
  <div class="callout" style="top:236px">Counterweight and Retainer Ring Assembly</div>
  <div class="callout" style="top:280px"><b>E Wall Thickness</b><br>Alloy 6063-T6 Tapered Aluminum Tube</div>
  <div class="callout" style="top:326px">Flush Access Door with Keyed Lock,<br>Continuous Piano Hinge, and Manually<br>Operated Cam Cleat</div>
  <div class="callout" style="top:366px"><b>D Butt Diameter</b></div>
  <div class="callout" style="top:383px"><b>Aluminum Collar</b> (Options Available)<br>See Specification Box<br>Perimeter caulked by Installer</div>
  <div class="callout" style="top:408px">2" Cap - Cement or Waterproof Compound<br>and Hardwood Wedges (By Installer)</div>
  <div class="callout" style="top:423px">Ground Sleeve Assembly - 16 Gauge Galvanized Steel Tube</div>
  <div class="callout" style="top:431px;width:70px">Tamped Dry Sand (By Installer)</div>
  <div class="callout" style="top:442px;width:70px">3/16" Steel Plate Welded to Sleeve</div>
  <div class="callout" style="top:450px;width:70px">3/16" Steel Support Plate</div>
  <div class="callout" style="top:457px;width:70px">Lightning Spike -<br>3/4" Diameter Steel Rod</div>
  <div class="note"><b>Note:</b> Foundation design not included. Foundation dimensions should be determined by a qualified Engineer familiar with site soil conditions.</div>

  <div class="partno partno--model">HCP35C61</div>
  <span class="partno__dash">-</span>
  <div class="partno partno--finish">SAT</div>

  <div class="product" style="left:258px;top:176px"><div class="product__img img-truck" role="img" aria-label="Revolving flagpole truck photo"></div><div class="product__code">RT-4410</div>Int. Revolving Truck<br>Sealed Bearings</div>
  <div class="product" style="left:330px;top:176px"><div class="product__img img-ball" role="img" aria-label="Gold ball ornament photo"></div><div class="product__code">ORN-0612-GLD</div>HD Gold Anodized<br>Aluminum Ball</div>
  <div class="product" style="left:258px;top:277px"><div class="product__img img-collar" role="img" aria-label="Spun aluminum collar photo"></div><div class="product__code">CLR-206S</div>Spun Aluminum Collar<br>1-Piece</div>
  <div class="product" style="left:330px;top:277px"><div class="product__img img-satin" role="img" aria-label="Satin aluminum finish sample"></div><div class="product__code">SAT</div>Satin Finish</div>
  <div class="product" style="left:258px;top:371px"><div class="product__img img-cleat" role="img" aria-label="Flush mount cam cleat door photo"></div><div class="product__code">FCD - CAM CLEAT</div>Flush Mount<br>Hinged Door</div>

  <div class="footer"></div>
  <div class="footer__brand">Ridgeline<small>Flag &amp; Flagpole</small></div>
  <div class="footer__address">418 Cedar Hollow Rd, Dalton, TX 78600</div>
  <div class="footer__contact">
    <div><svg viewBox="0 0 10 10"><path d="M2 0.5 3.8 2.6 2.9 4Q4 6.3 6 7.1L7.4 6.2 9.5 8 8.3 9.5Q1 8 0.5 1.7Z"/></svg>555-201-4477</div>
    <div><svg viewBox="0 0 10 10"><path d="M0 2h10v6H0z M0 2l5 3.5L10 2" fill="#fff" stroke="#8a1a1e" stroke-width="0.8"/></svg>info@ridgelineflag.com</div>
  </div>
</section>

<section class="page page--specs">
  <h1 class="specs__title">Heritage Series - HRW <span>Internal Reinforced with Winch - Wire Halyard</span></h1>
  <table class="spec-table">
    <colgroup><col style="width:24px"><col style="width:24px"><col style="width:46px"><col style="width:45px"><col style="width:37px"><col style="width:34px"><col style="width:40px"><col style="width:39px"><col style="width:33px"><col style="width:76px"></colgroup>
    <thead><tr><th>Mtg.<br>Hgt.</th><th>Butt<br>Dia.</th><th>Wall<br>Thickness</th><th>Pole<br>Sections</th><th>Set<br>Depth</th><th>Top<br>Diam.</th><th>Std. Flag<br>Size</th><th colspan="2">Max Wind Speed<br><small>With Nylon Flag</small> <small>No Flag</small></th><th>Catalog Number<br>****Specify Finish</th></tr></thead>
    <tbody>
<tr><td>20'</td><td>6"</td><td>.156"</td><td>1</td><td>2'-0"</td><td>3.5"</td><td>4' x 6'</td><td>208</td><td>301</td><td class="cat">HRW20C61-***</td></tr>
<tr><td></td><td>6"</td><td>.188"</td><td>1</td><td>2'-0"</td><td>3.5"</td><td>4' x 6'</td><td>229</td><td>328</td><td class="cat">HRW20D61-***</td></tr>
<tr><td>25'</td><td>6"</td><td>.156"</td><td>1</td><td>2'-6"</td><td>3.5"</td><td>5' x 8'</td><td>149</td><td>230</td><td class="cat">HRW25C61-***</td></tr>
<tr><td></td><td>6"</td><td>.188"</td><td>1</td><td>2'-6"</td><td>3.5"</td><td>5' x 8'</td><td>168</td><td>253</td><td class="cat">HRW25D61-***</td></tr>
<tr><td>30'</td><td>6"</td><td>.156"</td><td>1</td><td>3'-0"</td><td>3.5"</td><td>6' x 10'</td><td>108</td><td>174</td><td class="cat">HRW30C61-***</td></tr>
<tr><td></td><td>6"</td><td>.156"</td><td>2</td><td>3'-0"</td><td>3.5"</td><td>6' x 10'</td><td>108</td><td>174</td><td class="cat">HRW30C62-***</td></tr>
<tr><td></td><td>6"</td><td>.188"</td><td>1</td><td>3'-0"</td><td>3.5"</td><td>6' x 10'</td><td>122</td><td>197</td><td class="cat">HRW30D61-***</td></tr>
<tr><td></td><td>6"</td><td>.188"</td><td>2</td><td>3'-0"</td><td>3.5"</td><td>6' x 10'</td><td>122</td><td>197</td><td class="cat">HRW30D62-***</td></tr>
<tr><td></td><td>7"</td><td>.188"</td><td>1</td><td>3'-0"</td><td>3.5"</td><td>6' x 10'</td><td>157</td><td>235</td><td class="cat">HRW30D71-***</td></tr>
<tr><td></td><td>7"</td><td>.188"</td><td>2</td><td>3'-0"</td><td>3.5"</td><td>6' x 10'</td><td>157</td><td>235</td><td class="cat">HRW30D72-***</td></tr>
<tr><td>35'</td><td>6"</td><td>.156"</td><td>1</td><td>3'-6"</td><td>3.5"</td><td>6' x 10'</td><td>87</td><td>116</td><td class="cat">HRW35C61-***</td></tr>
<tr><td></td><td>6"</td><td>.156"</td><td>2</td><td>3'-6"</td><td>3.5"</td><td>6' x 10'</td><td>87</td><td>116</td><td class="cat">HRW35C62-***</td></tr>
<tr><td></td><td>6"</td><td>.188"</td><td>1</td><td>3'-6"</td><td>3.5"</td><td>6' x 10'</td><td>97</td><td>145</td><td class="cat">HRW35D61-***</td></tr>
<tr><td></td><td>6"</td><td>.188"</td><td>2</td><td>3'-6"</td><td>3.5"</td><td>6' x 10'</td><td>97</td><td>145</td><td class="cat">HRW35D62-***</td></tr>
<tr><td></td><td>6"</td><td>.156"</td><td>1</td><td>3'-6"</td><td>3.5"</td><td>6' x 10'</td><td>110</td><td>165</td><td class="cat">HRW35C71-***</td></tr>
<tr><td></td><td>6"</td><td>.156"</td><td>2</td><td>3'-6"</td><td>3.5"</td><td>6' x 10'</td><td>110</td><td>165</td><td class="cat">HRW35C72-***</td></tr>
<tr><td></td><td>7"</td><td>.188"</td><td>1</td><td>3'-6"</td><td>3.5"</td><td>6' x 10'</td><td>127</td><td>187</td><td class="cat">HRW35D71-***</td></tr>
<tr><td></td><td>7"</td><td>.188"</td><td>2</td><td>3'-6"</td><td>3.5"</td><td>6' x 10'</td><td>127</td><td>187</td><td class="cat">HRW35D72-***</td></tr>
<tr><td></td><td>7"</td><td>.188"</td><td>1</td><td>3'-6"</td><td>3.5"</td><td>6' x 10'</td><td>127</td><td>187</td><td class="cat">HRW35D71-***</td></tr>
<tr><td>40'</td><td>7"</td><td>.188"</td><td>2</td><td>3'-6"</td><td>3.5"</td><td>6' x 10'</td><td>127</td><td>187</td><td class="cat">HRW35D72-***</td></tr>
<tr><td></td><td>8"</td><td>.188"</td><td>1</td><td>3'-6"</td><td>4"</td><td>6' x 10'</td><td>155</td><td>213</td><td class="cat">HRW35D81-***</td></tr>
<tr><td></td><td>7"</td><td>.156"</td><td>1</td><td>4'-0"</td><td>3.5"</td><td>8' x 12'</td><td>87</td><td>122</td><td class="cat">HRW40C71-***</td></tr>
<tr><td></td><td>7"</td><td>.156"</td><td>2</td><td>4'-0"</td><td>3.5"</td><td>8' x 12'</td><td>87</td><td>122</td><td class="cat">HRW40C72-***</td></tr>
<tr><td></td><td>7"</td><td>.188"</td><td>1</td><td>4'-0"</td><td>3.5"</td><td>8' x 12'</td><td>98</td><td>147</td><td class="cat">HRW40D71-***</td></tr>
<tr><td></td><td>8"</td><td>.156"</td><td>1</td><td>4'-0"</td><td>4"</td><td>8' x 12'</td><td>107</td><td>157</td><td class="cat">HRW40C81-***</td></tr>
<tr><td></td><td>8"</td><td>.156"</td><td>2</td><td>4'-0"</td><td>3.5"</td><td>8' x 12'</td><td>107</td><td>157</td><td class="cat">HRW40C82-***</td></tr>
<tr><td>45'</td><td>8"</td><td>.188"</td><td>1</td><td>4'-0"</td><td>4"</td><td>8' x 12'</td><td>123</td><td>177</td><td class="cat">HRW40D81-***</td></tr>
<tr><td></td><td>8"</td><td>.188"</td><td>2</td><td>4'-0"</td><td>3.5"</td><td>8' x 12'</td><td>122</td><td>177</td><td class="cat">HRW40D82-***</td></tr>
<tr><td></td><td>8"</td><td>.188"</td><td>2</td><td>4'-0"</td><td>4"</td><td>8' x 12'</td><td>166</td><td>226</td><td class="cat">HRW40D12-***</td></tr>
<tr><td>50'</td><td>10"</td><td>.188"</td><td>2</td><td>4'-0"</td><td>4"</td><td>8' x 12'</td><td>102</td><td>144</td><td class="cat">HRW45D82-***</td></tr>
<tr><td></td><td>8"</td><td>.188"</td><td>2</td><td>4'-6"</td><td>3.5"</td><td>8' x 12'</td><td>125</td><td>173</td><td class="cat">HRW45F82-***</td></tr>
<tr><td></td><td>8"</td><td>.250"</td><td>2</td><td>4'-6"</td><td>3.5"</td><td>8' x 12'</td><td>143</td><td>192</td><td class="cat">HRW45D12-***</td></tr>
<tr><td>55'</td><td>10"</td><td>.188"</td><td>2</td><td>4'-6"</td><td>4"</td><td>8' x 12'</td><td>83</td><td>117</td><td class="cat">HRW50D83-***</td></tr>
<tr><td>60'</td><td>8"</td><td>.188"</td><td>3</td><td>5'-0"</td><td>3.5"</td><td>10' x 15'</td><td>118</td><td>164</td><td class="cat">HRW50D13-***</td></tr>
<tr><td>65'</td><td>10"</td><td>.188"</td><td>3</td><td>5'-0"</td><td>4"</td><td>10' x 15'</td><td>140</td><td>191</td><td class="cat">HRW50F13-***</td></tr>
<tr><td>70'</td><td>10"</td><td>.250"</td><td>3</td><td>5'-0"</td><td>4"</td><td>10' x 15'</td><td>102</td><td>139</td><td class="cat">HRW55D13-***</td></tr>
    </tbody>
  </table>
</section>

</body>
</html>
```